K & T Fabrication Web Design | ||
Web Template | ||
Manufacturing | ||
www.kandtfab.example | ||
The current business that I am purchasing is a run of the mill, precision metal machining and manufacturing company. The owner is retirement age and it's my objective to make it new school and cutting edge. I want professional, eye catching concepts that capture what I am trying to do with the traditionally old school industry. I want to appeal to the younger engineers in the industry. I want to illustrate the professional, cutting edge services I intend to offer through my company. I want to show that we are not the traditional, dirty old machine shop. We are a company run by a young, fast-paced engineer focused on providing the highest quality work in the industry. | ||
I would like to have a navigation bar that contains "HOME", "CAPABILITIES", "PROJECTS", "ABOUT US", and "CONTACT US" tabs. I like un-cluttered websites that deliver a clear message that the company has an organized, structured leadership in place. I want to show that the machining industry is not always old, dirty, and antiquated. My company is cutting edge, engineering driven, and able to meet the customer's every demand. | ||
Cutting-Edge Unique/Creative Clean/Simple Professional Sophisticated Modern Industrial Progressive High Tech Masculine |
Black/Charcoal | ||
above header | ||
http://www.pellworth-clinical.example/ | ||
http://world.varnick-ostley.example/master/6600.htm | ||
http://brockmoorlifts.example/ | ||
Please attempt to match font type of the uploaded business card and company logo designs. I would like to have a seamless design throughout. | ||

```html
<!DOCTYPE html>
<html lang="en">
<head>
<meta charset="utf-8">
<title>K &amp; T Fabrication</title>
<link rel="stylesheet" href="https://fonts.googleapis.com/css2?family=Arimo:wght@400;700&display=swap">
<style>
  :root {
    --blue: #1b6fc2;
    --blue-bright: #2f8fe3;
    --blue-deep: #0d2f63;
    --navy: #0a1f44;
    --text: #4a4a4a;
    --muted: #777;
    --light: #f1f2f4;
    --line: #d9dadd;
    --charcoal: #2a2a2b;
    --white: #fff;
  }
  * { box-sizing: border-box; margin: 0; padding: 0; }
  html, body { width: 1200px; height: 876px; overflow: hidden; }
  body { font-family: "Arimo", Arial, sans-serif; color: var(--text); background: var(--white); position: relative; }

  .header { position: absolute; top: 0; left: 0; width: 1200px; height: 120px; background: var(--white); }
  .brand { position: absolute; left: 240px; top: 30px; display: flex; align-items: center; gap: 12px; }
  .brand-mark { width: 56px; height: 56px; border-radius: 50%; background: #8d9299; }
  .brand-name { font-size: 25px; font-weight: 700; color: var(--blue); text-transform: uppercase; letter-spacing: 0.5px; line-height: 1; }
  .brand-tagline { font-size: 8px; color: var(--muted); text-transform: uppercase; letter-spacing: 1px; margin-top: 4px; }

  .search { position: absolute; left: 818px; top: 14px; width: 110px; height: 20px; border: 1px solid var(--line); border-radius: 10px; background: var(--white); }
  .search svg { position: absolute; right: 6px; top: 4px; }
  .phone { position: absolute; left: 850px; top: 58px; font-size: 15px; color: var(--text); display: flex; align-items: center; gap: 6px; }

  .nav { position: absolute; left: 612px; top: 95px; display: flex; gap: 4px; }
  .nav a { display: block; padding: 0 10px; height: 25px; line-height: 25px; font-size: 12px; font-weight: 700; color: var(--blue-deep); text-decoration: none; border-radius: 3px 3px 0 0; }
  .nav a.active { background: var(--blue); color: var(--white); }

  .hero { position: absolute; top: 120px; left: 0; width: 1200px; height: 270px; background: linear-gradient(180deg, var(--blue) 0%, var(--blue-deep) 55%, var(--navy) 100%); }
  .slider { position: absolute; left: 240px; top: 12px; width: 716px; height: 240px; background: #0c1c33; border: 1px solid #3c5a85; box-shadow: 0 4px 14px rgba(0,0,0,.45); overflow: hidden; }
  .slide-copy { position: absolute; left: 0; top: 0; width: 264px; height: 238px; padding: 22px 18px; background: linear-gradient(180deg, #1d2736, #0b121c); }
  .slide-title { color: var(--white); font-size: 20px; line-height: 1.25; }
  .slide-text { color: #d3d9e2; font-size: 11px; line-height: 1.45; margin-top: 12px; }
  .btn-learn { position: absolute; left: 18px; top: 190px; width: 118px; height: 30px; border-radius: 4px; background: linear-gradient(180deg, var(--blue-bright), var(--blue)); color: var(--white); font-size: 13px; font-weight: 700; display: flex; align-items: center; gap: 8px; padding-left: 8px; }
  .btn-learn .dot { width: 18px; height: 18px; border-radius: 50%; background: var(--white); display: flex; align-items: center; justify-content: center; }
  .slide-photo { position: absolute; left: 264px; top: 0; width: 450px; height: 238px; background: linear-gradient(180deg, #7a8ea3 0%, #5b6a78 45%, #3a3f48 100%); }
  .slide-arrows { position: absolute; right: 12px; bottom: 12px; display: flex; gap: 6px; }
  .slide-arrows span { width: 22px; height: 22px; border-radius: 50%; background: #e6e6e6; display: flex; align-items: center; justify-content: center; }

  .content { position: absolute; top: 390px; left: 0; width: 1200px; height: 330px; background: linear-gradient(180deg, #f7f8f9, var(--white) 30%); }
  .welcome { position: absolute; left: 244px; top: 18px; width: 712px; }
  .welcome h1 { font-size: 16px; font-weight: 400; color: var(--text); display: flex; align-items: center; gap: 8px; }
  .welcome h1 b { color: var(--blue); font-weight: 400; }
  .welcome h1 .bullet { width: 16px; height: 16px; border-radius: 50%; background: var(--blue-bright); border: 3px solid #cfe2f5; }
  .welcome p { font-size: 10px; line-height: 1.4; color: var(--muted); margin-top: 10px; }

  .cards { position: absolute; left: 240px; top: 158px; width: 716px; display: flex; gap: 22px; }
  .card { background: linear-gradient(180deg, #eef0f2, var(--white)); border: 1px solid var(--line); height: 148px; padding: 10px 14px; position: relative; }
  .card.who { width: 228px; }
  .card.cap { width: 218px; }
  .card.proj { width: 226px; }
  .card h2 { font-size: 13px; font-weight: 400; color: var(--text); display: flex; align-items: center; gap: 6px; margin-bottom: 8px; }
  .card h2 b { color: var(--blue); font-weight: 400; }
  .card h2 .bullet { width: 12px; height: 12px; border-radius: 50%; background: var(--blue-bright); border: 2px solid #cfe2f5; }
  .card p { font-size: 9px; line-height: 1.45; color: var(--muted); }
  .card .more { position: absolute; right: 14px; bottom: 8px; font-size: 9px; color: var(--blue); }
  .card ul { list-style: none; }
  .card li { font-size: 9px; line-height: 11px; color: var(--muted); padding: 3px 0; border-bottom: 1px solid var(--line); }
  .card li::before { content: "› "; color: var(--blue); }

  .footer { position: absolute; top: 720px; left: 0; width: 1200px; height: 156px; background: var(--charcoal); }
  .footer h3 { font-size: 13px; font-weight: 400; color: var(--blue-bright); }
  .foot-nav { position: absolute; left: 246px; top: 14px; }
  .foot-nav ul { list-style: none; margin-top: 10px; }
  .foot-nav li { font-size: 9px; color: var(--white); line-height: 20px; }
  .newsletter { position: absolute; left: 432px; top: 14px; }
  .newsletter .field { width: 180px; height: 22px; margin-top: 18px; background: var(--white); border: 1px solid #999; font-size: 9px; color: var(--muted); padding: 5px 6px; }
  .btn-sub { margin: 14px 0 0 140px; width: 108px; height: 30px; border-radius: 4px; background: linear-gradient(180deg, var(--blue-bright), var(--blue)); color: var(--white); font-size: 13px; display: flex; align-items: center; gap: 8px; padding-left: 8px; }
  .btn-sub .dot { width: 18px; height: 18px; border-radius: 50%; background: var(--white); display: flex; align-items: center; justify-content: center; }
  .divider { position: absolute; left: 732px; top: 14px; width: 1px; height: 126px; background: #4a4a4b; }
  .foot-brand { position: absolute; left: 816px; top: 24px; }
  .foot-brand .row { display: flex; align-items: center; gap: 8px; }
  .foot-brand .mark { width: 36px; height: 36px; border-radius: 50%; background: #8d9299; }
  .foot-brand .name { font-size: 15px; font-weight: 700; color: var(--white); text-transform: uppercase; }
  .copyright { font-size: 9px; color: var(--white); line-height: 1.4; margin-top: 20px; }
</style>
</head>
<body>
  <header class="header">
    <div class="brand">
      <div class="brand-mark"></div>
      <div>
        <div class="brand-name">K &amp; T Fabrication</div>
        <div class="brand-tagline">Precision products and engineered solutions</div>
      </div>
    </div>
    <div class="search">
      <svg width="12" height="12" viewBox="0 0 12 12"><circle cx="5" cy="5" r="3.5" fill="none" stroke="#1b6fc2" stroke-width="1.5"/><line x1="7.6" y1="7.6" x2="11" y2="11" stroke="#1b6fc2" stroke-width="1.5"/></svg>
    </div>
    <div class="phone">
      <svg width="14" height="14" viewBox="0 0 14 14"><path d="M3 1h3l1 3-2 1c1 2 2 3 4 4l1-2 3 1v3c0 1-1 2-2 2C6 13 1 8 1 3c0-1 1-2 2-2z" fill="#777"/></svg>
      (555) 014-2760
    </div>
    <nav class="nav">
      <a class="active" href="#">Home</a>
      <a href="#">About Us</a>
      <a href="#">Capabilities</a>
      <a href="#">Projects</a>
      <a href="#">Contact Us</a>
    </nav>
  </header>

  <section class="hero">
    <div class="slider">
      <div class="slide-copy">
        <div class="slide-title">Precision Products and<br>Engineerd Solutions</div>
        <p class="slide-text">Lorem ipsum dolor sit amet, consectetur adipisicing elit, sed do eiusmod tempor incididunt ut labore et dolore magna aliqua. Ut enim ad minim veniam.</p>
      </div>
      <div class="btn-learn"><span class="dot"><svg width="8" height="8" viewBox="0 0 8 8"><path d="M2 1l4 3-4 3z" fill="#1b6fc2"/></svg></span>Learn More</div>
      <div class="slide-photo" role="img" aria-label="Photo of a bright, organised machining shop floor with rows of machines"></div>
      <div class="slide-arrows">
        <span><svg width="8" height="8" viewBox="0 0 8 8"><path d="M6 1L2 4l4 3z" fill="#333"/></svg></span>
        <span><svg width="8" height="8" viewBox="0 0 8 8"><path d="M2 1l4 3-4 3z" fill="#333"/></svg></span>
      </div>
    </div>
  </section>

  <main class="content">
    <div class="welcome">
      <h1><span class="bullet"></span>Welcome to <b>K &amp; T Fabrication</b></h1>
      <p>Lorem ipsum dolor sit amet, consectetur adipisicing elit, sed do eiusmod tempor incididunt ut labore et dolore magna aliqua. Ut enim ad minim veniam, quis nostrud exercitation ullamco laboris nisi ut aliquip ex ea commodo consequat.</p>
      <p>Lorem ipsum dolor sit amet, consectetur adipisicing elit, sed do eiusmod tempor incididunt ut labore et dolore magna aliqua. Ut enim ad minim veniam, quis nostrud exercitation ullamco laboris nisi ut aliquip ex ea commodo consequat. Duis aute irure dolor in reprehenderit in voluptate velit esse cillum dolore eu fugiat nulla pariatur. Excepteur sint occaecat cupidatat non proident, sunt in culpa qui officia deserunt mollit.</p>
    </div>
    <div class="cards">
      <div class="card who">
        <h2><span class="bullet"></span>Who <b>We are</b></h2>
        <p>Lorem ipsum dolor sit amet, consectetur adipisicing elit, sed do eiusmod tempor incididunt ut labore et dolore magna aliqua. Ut enim ad minim veniam, quis nostrud exercitation ullamco laboris nisi ut aliquip ex ea commodo consequat.</p>
        <span class="more">[Read More]</span>
      </div>
      <div class="card cap">
        <h2><span class="bullet"></span><b>Capabilities</b></h2>
        <p>Lorem ipsum dolor sit amet, consectetur adipisicing elit.</p>
        <p style="margin-top:8px">sed do eiusmod tempor incididunt ut labore et dolore magna aliqua. Ut enim ad minim veniam, quis nostrud.</p>
        <span class="more">[Read More]</span>
      </div>
      <div class="card proj">
        <h2><span class="bullet"></span>Our <b>Projects</b></h2>
        <ul>
          <li>Lorem ipsum dolor sit amet</li>
          <li>consectetur adipisicing elit sed</li>
          <li>do eiusmod tempor</li>
          <li>incididunt ut labore</li>
          <li>labore et dolore magna aliqua</li>
        </ul>
        <span class="more">[Read More]</span>
      </div>
    </div>
  </main>

  <footer class="footer">
    <div class="foot-nav">
      <h3>Navigation</h3>
      <ul>
        <li>Home</li>
        <li>About Us</li>
        <li>Capabilities</li>
        <li>Projects</li>
        <li>Contact Us</li>
      </ul>
    </div>
    <div class="newsletter">
      <h3>Subscribe Newsletter</h3>
      <div class="field">Enter email address...</div>
      <div class="btn-sub"><span class="dot"><svg width="8" height="8" viewBox="0 0 8 8"><path d="M2 1l4 3-4 3z" fill="#1b6fc2"/></svg></span>Subscribe</div>
    </div>
    <div class="divider"></div>
    <div class="foot-brand">
      <div class="row"><div class="mark"></div><div class="name">K &amp; T Fabrication</div></div>
      <p class="copyright">Copyright © 2011 K &amp; T Fabrication.<br>All rights reserved.</p>
    </div>
  </footer>
</body>
</html>
```